velmorino.eu :: Design ideas (no coding) for key pages of Personalized greeting cards online store

We need your vision on modern, clean, easy to read user interface (UI) for online service of personalized printed products, like greeting cards, postcards, fridge magnets, clips and etc.
Your vision should include UI presentation for:
- Home page with login (including soc nets)
- Product Designer page
- Cart pages (products and address selection)
- Example of general internal page (pricing, terms, etc)
- Artist info and portfolio page
We are looking for ideas we will love, NOT complete design of a whole site.
Top design/vision will we used as a basement for separate contract on complete design of the site.

UI should be based on existing functionality with some extent. It should not break ideas or methods used on prototype but designers are free to offer own product presentations, designer’s layout and cart views.

Prototype:
English: http://velmorino.eu
Russian: http://velmorino.ru
Lithuanian: http://velmorino.lt

Target Market(s)

People of 16-45 y.o. who likes to be distinctive, personal.

Industry/Entity Type

Store

Requirements
Must have
• Your work should meet attached requirements.
Site is multilingual. Wording should assume varieties in length on different languages.
Clean and easy to read UI
Flat design preferrably
Should be based on assets which are free or available for royalty-free licensing
Should not have
• heavy, meaningless 3D and shadow effects
Show NOT copy sites like: plonkra.com, tarnwick.co.uk

```html
<!DOCTYPE html>
<html lang="en">
<head>
<meta charset="utf-8">
<title>velmorino — greeting cards store</title>
<link href="https://fonts.googleapis.com/css2?family=Open+Sans:wght@400;600;700&display=swap" rel="stylesheet">
<style>
:root{
  --red:#c8202f;
  --red-dark:#a3141f;
  --teal:#27b3a3;
  --ink:#333;
  --muted:#888;
  --line:#e3e3e3;
  --panel:#f4f4f4;
  --bg:#ffffff;
}
*{box-sizing:border-box;margin:0;padding:0}
html,body{width:758px;height:1200px;overflow:hidden}
body{position:relative;background:var(--bg);font-family:"Open Sans",Arial,sans-serif;color:var(--ink);font-size:8px}
.abs{position:absolute}

/* header */
.brand{left:14px;top:8px;width:70px;text-align:center}
.brand-mark{width:26px;height:26px;background:var(--red);margin:0 auto 3px}
.brand-name{font-size:13px;font-weight:700;color:var(--red)}
.tagline{left:96px;top:9px;font-size:13px;font-weight:700;color:var(--red)}
.welcome{left:250px;top:45px;font-size:7px;color:var(--muted);white-space:nowrap}
.welcome b{color:var(--red)}
.btn-contacts{left:470px;top:40px;background:var(--teal);color:#fff;font-size:8px;font-weight:700;padding:4px 10px;border-radius:2px}
.btn-cart{left:555px;top:40px;background:var(--red);color:#fff;font-size:8px;font-weight:700;padding:4px 10px;border-radius:2px}
.lang{left:610px;top:10px;width:80px;height:14px;border:1px solid var(--line);font-size:7px;color:var(--muted);padding:1px 4px}
.favs{left:650px;top:34px;width:50px;text-align:center;font-size:6px;color:var(--muted)}
.favs .circle{width:30px;height:30px;border:2px solid var(--red);border-radius:50%;margin:3px auto 0}

/* nav */
.nav{left:300px;top:108px;display:flex;gap:22px}
.nav a{font-size:8px;font-weight:600;color:var(--red);text-decoration:none;padding-bottom:3px}
.nav a.active{border-bottom:2px solid var(--red)}
.nav-rule{left:190px;top:123px;width:530px;height:1px;background:var(--line)}

/* sidebar */
.gallery-tab{left:50px;top:98px;width:132px;height:20px;background:var(--teal);color:#fff;font-size:9px;font-weight:700;padding:4px 8px}
.box{left:50px;width:132px;border:1px solid var(--line);background:#fff;overflow:hidden}
.box h3{font-size:9px;color:var(--red);padding:4px 6px;border-bottom:1px solid var(--line)}
.themes{top:130px;height:118px}
.tags{padding:5px 6px;display:flex;flex-wrap:wrap;gap:2px 4px;font-size:7px;line-height:10px}
.tags span{color:var(--muted)}
.tags span:nth-child(3n){color:var(--red)}
.tags span:nth-child(4n){color:var(--teal)}
.colors{top:254px;height:110px}
.swatches{display:grid;grid-template-columns:repeat(6,18px);gap:2px;padding:6px}
.swatches i{height:18px;display:block}

/* hero */
.hero{left:197px;top:128px;width:523px;height:246px;background:linear-gradient(120deg,#fbe9dc 0%,#f7d6c2 35%,#f9f1e6 60%,#f4c6d8 100%)}
.hero-text{left:430px;top:150px;text-align:center}
.hero-text h2{font-size:14px;font-weight:600;color:#fff;background:var(--red);padding:3px 10px}
.hero-text p{font-size:9px;color:var(--red);margin-top:4px}
.view-all{left:640px;top:380px;font-size:7px;color:var(--muted)}

/* grid */
.grid{left:50px;top:392px;width:670px;display:grid;grid-template-columns:repeat(4,160px);gap:10px 10px}
.card{height:190px;border:1px solid var(--line);background:#fff;display:flex;flex-direction:column}
.art{flex:1;margin:5px 5px 0}
.card-bar{height:26px;display:flex;align-items:center;gap:4px;padding:0 5px}
.price{background:#9a9a9a;color:#fff;font-weight:700;font-size:8px;padding:3px 8px;border-radius:2px}
.ico{width:14px;height:14px;border:1px solid #ccc;border-radius:50%}
.ico-sq{width:14px;height:14px;border:1px solid #ccc}
.promo{background:var(--red);color:#fff}
.promo .body{flex:1;padding:12px 10px}
.promo h4{font-size:12px;line-height:15px}
.promo .chips{margin-top:16px;display:flex;flex-wrap:wrap;gap:3px}
.promo .chips span{background:#e0505b;font-size:6px;padding:2px 4px}
.quad{display:grid;grid-template-columns:1fr 1fr;gap:4px;flex:1;margin:5px 5px 0}

/* pagination */
.pager{left:430px;top:990px;display:flex;gap:3px}
.pager span{border:1px solid var(--line);font-size:7px;color:var(--muted);padding:2px 5px;white-space:nowrap}
.pager span.on{background:var(--red);color:#fff;border-color:var(--red)}

/* footer */
.footer-rule{left:50px;top:1030px;width:670px;height:1px;background:var(--line)}
.links{top:1044px;list-style:none;font-size:7px;line-height:13px;color:var(--muted)}
.links li:first-child{color:var(--red);font-weight:700}
.follow{left:330px;top:1044px;font-size:9px;font-weight:700;color:var(--ink)}
.dots{left:330px;top:1062px;display:flex;gap:4px}
.dots i{width:12px;height:12px;border-radius:50%;background:#666;display:block}
.news{left:560px;top:1044px}
.news small{font-size:6px;color:var(--muted);display:block}
.news h4{font-size:11px;color:var(--red);margin:2px 0 5px}
.news .row{display:flex;gap:4px}
.news .field{width:110px;height:16px;border:1px solid var(--line);font-size:6px;color:#aaa;padding:3px}
.news .join{background:var(--red);color:#fff;font-size:7px;font-weight:700;padding:3px 8px}
.foot-brand{left:364px;top:1150px;width:30px;height:14px;background:var(--red)}
.copyright{left:0;top:1172px;width:758px;text-align:center;font-size:7px;color:var(--muted)}
</style>
</head>
<body>

<header>
  <div class="abs brand"><div class="brand-mark"></div><div class="brand-name">velmorino</div></div>
  <div class="abs tagline">The individual greeting cards according to your mood</div>
  <div class="abs lang">English ▾</div>
  <div class="abs welcome">Welcome visitor you can <b>LOG IN</b> or create an <b>ACCOUNT</b></div>
  <div class="abs btn-contacts">CONTACTS</div>
  <div class="abs btn-cart">Cart (0)</div>
  <div class="abs favs">Favorites (0)<div class="circle"></div></div>
</header>

<nav class="abs nav">
  <a class="active">ALL MEDIAS</a><a>GREETING CARDS</a><a>SQUARE CARDS</a><a>POSTCARDS</a>
</nav>
<div class="abs nav-rule"></div>

<aside>
  <div class="abs gallery-tab">Products Gallery</div>
  <div class="abs box themes">
    <h3>Themes</h3>
    <div class="tags">
      <span>All</span><span>Blues</span><span>Birthday</span><span>Love</span><span>Cakes</span><span>Christmas</span><span>Congratulations!</span><span>Dogs</span><span>Flowers</span><span>For children</span><span>Friendship</span><span>Love</span><span>Newborn</span><span>Photos</span><span>Religion</span><span>Sport</span><span>Thank you</span><span>Valentines</span><span>Wedding</span>
    </div>
  </div>
  <div class="abs box colors">
    <h3>Colors</h3>
    <div class="swatches">
      <i style="background:#e53935"></i><i style="background:#fb8c00"></i><i style="background:#fdd835"></i><i style="background:#43a047"></i><i style="background:#1e88e5"></i><i style="background:#8e24aa"></i>
      <i style="background:#ec407a"></i><i style="background:#ffb74d"></i><i style="background:#fff176"></i><i style="background:#81c784"></i><i style="background:#64b5f6"></i><i style="background:#ba68c8"></i>
      <i style="background:#6d4c41"></i><i style="background:#9e9e9e"></i><i style="background:#26a69a"></i><i style="background:#3949ab"></i><i style="background:#212121"></i><i style="background:#f5f5f5;border:1px solid #ddd"></i>
    </div>
  </div>
</aside>

<section class="abs hero" role="img" aria-label="Illustration of a woman in a sun hat beside a field of colourful flowers and a small bird"></section>
<div class="abs hero-text"><h2>Lorem ipsum dolor sit consectetur</h2><p>Proin feugiat quam quis metus porta</p></div>
<div class="abs view-all">View all designs</div>

<main class="abs grid">
  <div class="card promo">
    <div class="body">
      <h4>Lorem ipsum dolor sit<br>Lorem ipsum</h4>
      <div class="chips"><span>Birthday</span><span>Love</span><span>Flowers</span><span>Kids</span><span>Thank you</span><span>New</span></div>
    </div>
    <div class="card-bar"><span class="price">€48.00</span><span class="ico"></span><span class="ico-sq"></span></div>
  </div>
  <div class="card">
    <div class="quad" role="img" aria-label="Four small card designs: hearts, flowers and colourful patterns">
      <i style="background:#f4b6c8"></i><i style="background:#d95b7a"></i><i style="background:#6fbf73"></i><i style="background:#f0c24a"></i>
    </div>
    <div class="card-bar"><span class="price">€48.00</span><span class="ico"></span><span class="ico-sq"></span></div>
  </div>
  <div class="card"><div class="art" role="img" aria-label="Illustrated tree with swirling branches" style="background:linear-gradient(#e9c9a3,#8a9a6a)"></div><div class="card-bar"><span class="price">€48.00</span><span class="ico"></span><span class="ico-sq"></span></div></div>
  <div class="card"><div class="art" role="img" aria-label="Green hills landscape under a cloudy sky" style="background:linear-gradient(#b9d9ea,#7fb25a)"></div><div class="card-bar"><span class="price">€48.00</span><span class="ico"></span><span class="ico-sq"></span></div></div>

  <div class="card"><div class="art" role="img" aria-label="Colourful patchwork illustration" style="background:linear-gradient(135deg,#e85a4f,#f2c14e,#3a7bd5)"></div><div class="card-bar"><span class="price">€48.00</span><span class="ico"></span><span class="ico-sq"></span></div></div>
  <div class="card"><div class="art" role="img" aria-label="Cheerful clown with balloons" style="background:linear-gradient(#5fb04b,#e44b3c)"></div><div class="card-bar"><span class="price">€48.00</span><span class="ico"></span><span class="ico-sq"></span></div></div>
  <div class="card"><div class="art" role="img" aria-label="Black and white photo of two monkeys" style="background:linear-gradient(#d6d6d6,#6e6e6e)"></div><div class="card-bar"><span class="price">€48.00</span><span class="ico"></span><span class="ico-sq"></span></div></div>
  <div class="card"><div class="art" role="img" aria-label="Children's illustration with a ladybird on a leaf" style="background:linear-gradient(#f7e27a,#e3553f)"></div><div class="card-bar"><span class="price">€48.00</span><span class="ico"></span><span class="ico-sq"></span></div></div>

  <div class="card"><div class="art" role="img" aria-label="Teddy bear holding a heart" style="background:linear-gradient(#f3d3b0,#a9703f)"></div><div class="card-bar"><span class="price">€48.00</span><span class="ico"></span><span class="ico-sq"></span></div></div>
  <div class="card"><div class="art" role="img" aria-label="Snowy winter night with falling flakes" style="background:linear-gradient(#1f3c78,#c64a3a)"></div><div class="card-bar"><span class="price">€48.00</span><span class="ico"></span><span class="ico-sq"></span></div></div>
  <div class="card"><div class="art" role="img" aria-label="Photo of a wrinkled puppy" style="background:linear-gradient(#e3c9a6,#9b6a3c)"></div><div class="card-bar"><span class="price">€48.00</span><span class="ico"></span><span class="ico-sq"></span></div></div>
  <div class="card"><div class="art" role="img" aria-label="Painted winter village scene with figures" style="background:linear-gradient(#a9c4de,#c9b28a)"></div><div class="card-bar"><span class="price">€48.00</span><span class="ico"></span><span class="ico-sq"></span></div></div>
</main>

<div class="abs pager"><span>Page 1 to 150</span><span class="on">01</span><span>02</span><span>03</span><span>04</span><span>05</span><span>06</span><span>07</span><span>08</span><span>Last Page</span></div>

<footer>
  <div class="abs footer-rule"></div>
  <ul class="abs links" style="left:50px"><li>About us</li><li>How it works</li><li>Prices</li><li>Rules</li><li>Contacts</li></ul>
  <ul class="abs links" style="left:150px"><li>FAQ</li><li>Site Map</li><li>Privacy Policy</li><li>Terms of use</li><li>Help</li></ul>
  <div class="abs follow">FOLLOW US</div>
  <div class="abs dots"><i></i><i></i><i></i><i></i><i></i></div>
  <div class="abs news">
    <small>SIGN UP FOR NOTICE NEWS</small>
    <h4>NEWSLETTER</h4>
    <div class="row"><span class="field">Enter Email Address</span><span class="join">JOIN</span></div>
  </div>
  <div class="abs foot-brand"></div>
  <div class="abs copyright">Copyright © 2014 velmorino . All rights reserved.</div>
</footer>

</body>
</html>
```